“FB “ Hard Ice Tea -Fine Brew Tea

Looking for a pvc label for a 12oz slim can. Label must have ice tea with vodka on it. Also must have 5.5 alc.vol and 12oz (355ml).
On the back of must say distilled and bottled by Copper Hollow Mash Works inc.

Label should look like an old school New York deli with the attached photos as inspiration

Colors
0054AA
0677BA
7BADD7
CADEEF
E8F1F8

```html
<!DOCTYPE html>
<html lang="en">
<head>
<meta charset="UTF-8">
<title>FB Hard Ice Tea – Can Label</title>
<link href="https://fonts.googleapis.com/css2?family=Archivo+Black&family=DM+Serif+Display&display=swap" rel="stylesheet">
<style>
  :root {
    --navy: #0054AA;
    --ocean: #0677BA;
    --sky: #7BADD7;
    --mist: #CADEEF;
    --frost: #E8F1F8;
  }
  * { margin: 0; padding: 0; box-sizing: border-box; }
  html, body { width: 1200px; height: 600px; overflow: hidden; }
  body { background: var(--ocean); position: relative; }

  .label {
    position: absolute;
    left: 440px; top: 40px;
    width: 320px; height: 520px;
    background: var(--navy);
    overflow: hidden;
  }
  .label__pattern {
    position: absolute; inset: 0;
    background: linear-gradient(160deg, var(--frost) 0%, var(--sky) 50%, var(--mist) 100%);
  }
  .label__panel {
    position: absolute;
    left: 12px; top: 80px;
    width: 296px; height: 344px;
  }
  .badge-est {
    position: absolute; left: 50%; top: 126px;
    transform: translateX(-50%);
    font: 11px/1.2 "Archivo Black", sans-serif;
    color: var(--frost);
    border: 1.5px solid var(--frost);
    border-radius: 10px;
    padding: 2px 9px;
    letter-spacing: .5px;
    white-space: nowrap;
  }
  .badge-new {
    position: absolute; left: 252px; top: 100px;
    width: 56px; height: 56px;
  }
  .badge-new span {
    position: absolute; inset: 0;
    display: flex; align-items: center; justify-content: center;
    font: 17px "DM Serif Display", serif;
    color: var(--navy);
  }
  .brand-mark {
    position: absolute; left: 0; right: 0; top: 152px;
    text-align: center;
    font: 112px/1 "Archivo Black", sans-serif;
    color: var(--frost);
    letter-spacing: -4px;
  }
  .product-name {
    position: absolute; left: 0; right: 0; top: 276px;
    text-align: center;
    font: 24px/1 "Archivo Black", sans-serif;
    color: var(--frost);
    letter-spacing: 1px;
  }
  .product-type {
    position: absolute; left: 0; right: 0; top: 308px;
    text-align: center;
    font: 15px/1 "DM Serif Display", serif;
    color: var(--mist);
    letter-spacing: .5px;
  }
  .tagline {
    position: absolute; left: 36px; top: 340px;
    width: 248px; height: 44px;
    border: 2px solid var(--frost);
    border-radius: 22px;
    display: flex; align-items: center; justify-content: center;
    font: 23px/1 "DM Serif Display", serif;
    color: var(--frost);
    transform: rotate(-2deg);
    white-space: nowrap;
  }
  .distiller {
    position: absolute; left: 50%; bottom: 50px;
    transform: translateX(-50%);
    font: 10px/1.2 "DM Serif Display", serif;
    color: var(--frost);
    background: var(--navy);
    border-radius: 8px;
    padding: 3px 10px;
    white-space: nowrap;
  }
  .spec {
    position: absolute; bottom: 18px;
    font: 13px/1.2 "DM Serif Display", serif;
    color: var(--frost);
    background: var(--navy);
    border: 1.5px solid var(--frost);
    border-radius: 10px;
    padding: 2px 10px;
    white-space: nowrap;
  }
  .spec--abv { left: 14px; }
  .spec--volume { right: 14px; }
</style>
</head>
<body>
  <main class="label">
    <div class="label__pattern" role="img" aria-label="Blue and white deli checkerboard pattern"></div>

    <svg class="label__panel" viewBox="0 0 296 344" aria-hidden="true">
      <path fill="var(--navy)" d="M40 20 Q40 0 60 0 H236 Q256 0 256 20 V40 Q296 40 296 80 V304 Q296 344 256 344 H40 Q0 344 0 304 V80 Q0 40 20 40 Q40 40 40 20 Z"/>
    </svg>

    <div class="badge-est">est. 2024</div>

    <div class="badge-new">
      <svg viewBox="0 0 56 56" width="56" height="56" aria-hidden="true">
        <polygon points="28,2 52,14 52,42 28,54 4,42 4,14" fill="var(--frost)" stroke="var(--navy)" stroke-width="3"/>
      </svg>
      <span>New</span>
    </div>

    <div class="brand-mark">FB</div>
    <div class="product-name">HARD ICE TEA</div>
    <div class="product-type">Ice tea with vodka</div>
    <div class="tagline">Fine Brew Tea .</div>

    <div class="distiller">Distilled and bottled by Copper Hollow Mash Works inc.</div>
    <div class="spec spec--abv">5.5 alc.vol</div>
    <div class="spec spec--volume">12oz (355ml)</div>
  </main>
</body>
</html>
```